Business Card Design Project - bel soravin group

dear Sirs

we need business card design for our group ( BEL Soravin Group ) , i have got the Logo design of our group from pixel harbor in previous , so all need details relating to our group i think available with you, as well as the the chosen logo design

we hope to provide us with business card logo that to be appropaite and satisfactory to us .

thanks

note : logo design of our group is attached .
Updates

Reason: please extend the deadline of my project for additional 15 days because i didn't received appropriate design for our gruop yet . kindly beaware that i have received 77 design till now , supossed to send me 200-250 design at least . thanks

Target Market(s)

contents
-

name : Korvan EL Mistrani

position : Operation Manager

Industry/Entity Type

Business

Requirements
Must have

• person name

group logo
Nice to have
• logo color matching with back background

```html
<!DOCTYPE html>
<html lang="en">
<head>
<meta charset="utf-8">
<title>Korvan EL Mistrani – Business Card</title>
<link rel="stylesheet" href="https://fonts.googleapis.com/css2?family=Arimo:ital,wght@0,400;0,700;1,700&display=swap">
<style>
  :root {
    --card-white: #ffffff;
    --band-blue: #0037c8;
    --name-blue: #2a6cd2;
    --value-blue: #1f5cc8;
    --accent-cyan: #3cc6dc;
    --label-cyan: #45c2d8;
    --brand-blue: #1d3fc6;
  }
  html, body {
    margin: 0;
    padding: 0;
    overflow: hidden;
    background: var(--card-white);
  }
  .card {
    position: relative;
    width: 1200px;
    height: 686px;
    overflow: hidden;
    background: var(--card-white);
    font-family: "Arimo", Arial, sans-serif;
  }
  .card__band {
    position: absolute;
    inset: 0;
    width: 1200px;
    height: 686px;
  }
  .card__band polygon { fill: var(--band-blue); }

  .identity {
    position: absolute;
    right: 53px;
    top: 64px;
    text-align: right;
  }
  .identity__name {
    margin: 0;
    font-size: 38px;
    font-weight: 700;
    letter-spacing: 0.5px;
    color: var(--name-blue);
    text-transform: uppercase;
    line-height: 44px;
    white-space: nowrap;
  }
  .identity__role {
    margin: 0;
    font-size: 27px;
    font-weight: 700;
    font-style: italic;
    color: var(--accent-cyan);
    text-transform: uppercase;
    line-height: 36px;
    white-space: nowrap;
  }

  .contacts {
    position: absolute;
    left: 720px;
    right: 53px;
    top: 180px;
    margin: 0;
    padding: 0;
    list-style: none;
  }
  .contacts__row {
    display: flex;
    justify-content: space-between;
    align-items: baseline;
    gap: 12px;
    height: 39px;
  }
  .contacts__label {
    font-size: 20px;
    font-weight: 700;
    font-variant: small-caps;
    color: var(--label-cyan);
    line-height: 24px;
    white-space: nowrap;
  }
  .contacts__value {
    font-size: 21px;
    font-weight: 700;
    color: var(--value-blue);
    line-height: 24px;
    white-space: nowrap;
    text-align: right;
  }
  .contacts__value--web {
    font-size: 16px;
    letter-spacing: 0.4px;
  }

  .brand {
    position: absolute;
    left: 760px;
    top: 526px;
    display: flex;
    align-items: center;
    gap: 14px;
  }
  .brand__mark {
    width: 24px;
    height: 24px;
    background: var(--brand-blue);
  }
  .brand__name {
    font-size: 36px;
    font-weight: 700;
    color: var(--brand-blue);
    letter-spacing: 0.5px;
    white-space: nowrap;
  }
</style>
</head>
<body>
  <main class="card">
    <svg class="card__band" viewBox="0 0 1200 686" aria-hidden="true">
      <polygon points="194,0 657,0 526,589 1200,680 1200,686 51,686"/>
    </svg>

    <header class="identity">
      <h1 class="identity__name">Korvan EL Mistrani</h1>
      <p class="identity__role">Operation Manager</p>
    </header>

    <ul class="contacts">
      <li class="contacts__row"><span class="contacts__label">Tel :</span><span class="contacts__value">01234-56789-01234</span></li>
      <li class="contacts__row"><span class="contacts__label">Fax :</span><span class="contacts__value">01234-56789-01234</span></li>
      <li class="contacts__row"><span class="contacts__label">Mobile :</span><span class="contacts__value">01234-56789-01234</span></li>
      <li class="contacts__row"><span class="contacts__label">Email :</span><span class="contacts__value">kmistrani@belsoravingroup.com</span></li>
      <li class="contacts__row"><span class="contacts__label">Website :</span><span class="contacts__value contacts__value--web">WWW.BELSORAVINGROUP.COM</span></li>
      <li class="contacts__row"><span class="contacts__label">PO . Box :</span><span class="contacts__value"></span></li>
    </ul>

    <div class="brand">
      <span class="brand__mark" aria-hidden="true"></span>
      <span class="brand__name">BEL Soravin Group</span>
    </div>
  </main>
</body>
</html>
```